Service Plan Sales Flyer

The Watchpost Depot (www.kelvarnguard.com) is a commercial security integrator that installs security cameras, access control, intrusion, two-way radios and perimeter security. We require a one page flyer for our service plan for new and existing customers. The price of the service plan is $299/yr and includes the following;
1. Discounted service rate of $118/hr
2. Free remote support ($85/hr without a plan)
3. Free remote training
4. Priority support

Please review our brochure attached and create a one page sales flyer with the end goal of having the client sign up for our annual service plan . The plan will automatically renew every year. Email sales@kelvarnguard.com.

Target Market(s)

commercial industrial clients - no residential

Industry/Entity Type

review our website at www.kelvarnguard.com

Colors
0054AA
0677BA
7BADD7
CADEEF
E8F1F8
EE7325
F08F49
F5BC92
FAE3D3
FDF4ED

Requirements
Must have
• call to action
Should not have
• too many colors

```html
<!DOCTYPE html>
<html lang="en">
<head>
<meta charset="utf-8">
<title>The Watchpost Depot – Service Plan</title>
<link href="https://fonts.googleapis.com/css2?family=Montserrat:wght@300;400;500;700;800;900&display=swap" rel="stylesheet">
<style>
  :root {
    --red: #ee1d2b;
    --navy: #0b1c66;
    --white: #ffffff;
    --ink: #1b1f3a;
  }
  * { margin: 0; padding: 0; box-sizing: border-box; }
  html, body { width: 848px; height: 1200px; overflow: hidden; background: var(--white); }
  .flyer {
    position: relative; width: 848px; height: 1200px; overflow: hidden;
    background: var(--white); font-family: "Montserrat", sans-serif; color: var(--ink);
  }
  .hero-curve { position: absolute; left: 0; top: 0; width: 848px; height: 420px; }
  .brand {
    position: absolute; left: 60px; top: 68px; display: flex; align-items: center; gap: 10px;
  }
  .brand-mark { width: 30px; height: 30px; background: var(--navy); flex: none; }
  .brand-name {
    font-weight: 800; font-size: 21px; line-height: 23px; color: var(--navy); letter-spacing: 0.5px;
  }
  .product-visual {
    position: absolute; left: 340px; top: 72px; width: 390px; height: 252px; border-radius: 6px;
    background: linear-gradient(160deg, #f7f7f8 0%, #e6e7ea 55%, #cfd2d8 100%);
  }
  .price-badge {
    position: absolute; left: 631px; top: 327px; width: 166px; height: 166px; border-radius: 50%;
    background: var(--navy); box-shadow: 0 8px 10px rgba(0,0,0,0.25);
  }
  .price-badge-inner {
    position: absolute; left: 8px; top: 8px; width: 150px; height: 150px; border-radius: 50%;
    background: var(--red); color: var(--white); display: flex; flex-direction: column;
    align-items: center; justify-content: center; font-weight: 900; font-size: 21px; line-height: 1.3;
  }
  .price-badge-inner .per { font-size: 7px; font-weight: 700; margin: 0 2px; vertical-align: middle; }
  .headline { position: absolute; left: 50px; top: 419px; }
  .headline-lead {
    font-weight: 400; font-size: 21px; line-height: 26px; color: var(--navy); letter-spacing: 0.2px;
  }
  .headline-main {
    font-weight: 900; font-size: 43px; line-height: 48px; color: var(--red); letter-spacing: 0.3px;
  }
  .band {
    position: absolute; height: 37px; color: var(--white); font-weight: 800; font-size: 22px;
    display: flex; align-items: center;
  }
  .band-red { left: 0; width: 412px; background: var(--red); padding-left: 50px;
    clip-path: polygon(0 0, 100% 0, 90.3% 100%, 0 100%); }
  .band-navy { left: 439px; width: 409px; background: var(--navy); justify-content: flex-end; padding-right: 50px;
    clip-path: polygon(0 0, 100% 0, 100% 100%, 9.8% 100%); }
  .band-row-1 { top: 555px; }
  .band-row-2 { top: 766px; }
  .copy {
    position: absolute; font-weight: 400; font-size: 15px; line-height: 18.8px; color: var(--ink);
  }
  .copy-left { left: 50px; width: 322px; text-align: left; }
  .copy-right { right: 51px; width: 322px; text-align: right; }
  .copy-row-1 { top: 604px; }
  .copy-row-2 { top: 817px; }
  .rate {
    position: absolute; right: 505px; font-weight: 800; font-size: 21px; color: var(--red);
  }
  .rate-1 { top: 722px; }
  .rate-2 { top: 968px; }
  .cta {
    position: absolute; left: 0; top: 1017px; width: 848px; height: 71px; background: var(--red);
    text-align: center;
  }
  .cta-title {
    margin-top: 8px; font-weight: 900; font-size: 23px; line-height: 28px; color: var(--navy);
  }
  .cta-url { font-weight: 500; font-size: 22px; line-height: 28px; color: var(--white); }
  .note {
    position: absolute; left: 0; top: 1124px; width: 848px; text-align: center;
    font-weight: 500; font-size: 22px; color: var(--navy);
  }
  .note-label { font-weight: 900; color: var(--red); margin-right: 6px; }
</style>
</head>
<body>
<div class="flyer">
  <svg class="hero-curve" viewBox="0 0 848 420" aria-hidden="true">
    <defs>
      <linearGradient id="hero-fade" x1="0" y1="0" x2="0" y2="1">
        <stop offset="0" stop-color="#ffffff"/>
        <stop offset="0.6" stop-color="#fbfbfc"/>
        <stop offset="1" stop-color="#ececef"/>
      </linearGradient>
    </defs>
    <path d="M0,122 Q424,648 848,122 L848,0 L0,0 Z" fill="var(--red)"/>
    <path d="M60,190 Q424,544 788,190 Z" fill="var(--navy)"/>
    <path d="M0,118 Q424,585 848,118 L848,0 L0,0 Z" fill="url(#hero-fade)"/>
  </svg>

  <div class="brand">
    <span class="brand-mark"></span>
    <span class="brand-name">THE WATCHPOST<br>DEPOT</span>
  </div>

  <div class="product-visual" role="img" aria-label="Security products: a door with access control reader, a monitor showing video management software, a dome camera and a bullet camera"></div>

  <div class="price-badge">
    <div class="price-badge-inner">
      <span>PRICE:</span>
      <span>$299<span class="per">per</span>year</span>
    </div>
  </div>

  <div class="headline">
    <p class="headline-lead">SECURE YOUR BUSINESS</p>
    <p class="headline-lead">WITH OUR COMPREHENSIVE</p>
    <h1 class="headline-main">SERVICE PLAN</h1>
  </div>

  <h2 class="band band-red band-row-1">Discounted Service Rate:</h2>
  <p class="copy copy-left copy-row-1">Receive a discounted service rate of $118/hour for any security-related services provided by The Watchpost Depot. This reduced rate ensures cost-effective support and maintenance for your security systems.</p>
  <p class="rate rate-1">$118 per hour</p>

  <h2 class="band band-navy band-row-1">Free Remote Training:</h2>
  <p class="copy copy-right copy-row-1">Take advantage of our complimentary remote training sessions. Our experienced trainers will guide you through the operation and management of your security systems, ensuring you have the knowledge and confidence to utilize them effectively.</p>

  <h2 class="band band-red band-row-2">Free Remote Support:</h2>
  <p class="copy copy-left copy-row-2">Enjoy free remote support from our expert technicians. Our team will assist you remotely with any technical issues or questions you may have regarding your security systems. Without a service plan, remote support is billed at $85/hour, so this benefit saves you money.</p>
  <p class="rate rate-2">$85 per hour</p>

  <h2 class="band band-navy band-row-2">Priority Support:</h2>
  <p class="copy copy-right copy-row-2">As a service plan subscriber, you will receive priority support. Your inquiries and requests will be given expedited attention, ensuring prompt assistance and minimizing any downtime or disruptions to your security systems.</p>

  <div class="cta">
    <p class="cta-title">GET STARTED WITH OUR SERVICE PLAN NOW</p>
    <p class="cta-url">www.kelvarnguard.com</p>
  </div>

  <p class="note"><span class="note-label">NOTE:</span>The plan will automatically renew every year</p>
</div>
</body>
</html>
```